Business Cards/Letterhead for Electrical Contractor
Electrical Contractor
Business Cards/Letterhead for Electrical Contractor - Construction
Creative Brief
Use same font as used in my logo
A combination may be used
Modern
Derek Stallworth
President
48306 Calloway Avenue Westminster, Colorado 80234
derek@quorvantpower.example

```html
<!DOCTYPE html>
<html lang="en">
<head>
<meta charset="utf-8">
<title>Quorvant Power, Inc. — Business Card</title>
<link rel="stylesheet" href="https://fonts.googleapis.com/css2?family=Aldrich&display=swap">
<style>
  :root {
    --backdrop: #e4e6e8;
    --card: #ffffff;
    --brand-blue: #3a8fd6;
    --ink-dark: #474c52;
    --ink-mid: #6d737a;
    --rule: #3d4248;
  }
  * { margin: 0; padding: 0; box-sizing: border-box; }
  html, body {
    width: 1200px; height: 946px; overflow: hidden;
    background: var(--backdrop);
    font-family: "Aldrich", sans-serif;
  }
  .canvas { position: relative; width: 1200px; height: 946px; }
  .card {
    position: absolute; left: 250px; width: 700px; height: 400px;
    background: var(--card); border-radius: 22px;
    box-shadow: 0 8px 24px rgba(0,0,0,0.12);
  }
  .card--back { top: 49px; }
  .card--front { top: 497px; }

  /* back */
  .back-mark {
    position: absolute; left: 0; right: 0; top: 150px;
    display: flex; justify-content: center; align-items: center; gap: 16px;
  }
  .mark-square {
    width: 44px; height: 44px; border-radius: 8px; background: var(--brand-blue);
  }
  .back-mark .wordmark { font-size: 34px; color: var(--brand-blue); letter-spacing: 2px; }
  .social-list {
    position: absolute; right: 34px; bottom: 28px;
    display: flex; gap: 22px; list-style: none;
  }
  .social-item { display: flex; align-items: center; gap: 7px; font-size: 12px; color: var(--ink-mid); }
  .social-square { width: 16px; height: 16px; border-radius: 2px; background: var(--brand-blue); }

  /* front */
  .brand-block {
    position: absolute; left: 48px; top: 120px; width: 270px;
  }
  .brand-block .mark-square { width: 58px; height: 58px; margin-bottom: 18px; }
  .brand-name { font-size: 38px; color: var(--ink-dark); letter-spacing: 3px; line-height: 1; }
  .brand-sub { font-size: 20px; color: var(--ink-dark); letter-spacing: 6px; margin-top: 8px; }

  .details { position: absolute; left: 360px; top: 58px; width: 320px; }
  .detail-row { display: flex; align-items: center; margin-bottom: 30px; }
  .detail-icon { width: 34px; height: 34px; flex: none; }
  .detail-rule { width: 3px; align-self: stretch; background: var(--rule); margin: 0 16px 0 14px; }
  .detail-text { font-size: 14px; color: var(--ink-mid); line-height: 1.6; }
  .person-name { font-size: 24px; color: var(--brand-blue); letter-spacing: 1px; line-height: 1.2; }
  .person-title { font-size: 14px; color: var(--ink-mid); }
</style>
</head>
<body>
<main class="canvas">
  <section class="card card--back" aria-label="Card back">
    <div class="back-mark">
      <span class="mark-square"></span>
      <span class="wordmark">QUORVANT</span>
    </div>
    <ul class="social-list">
      <li class="social-item"><span class="social-square"></span>/tmarrowby</li>
      <li class="social-item"><span class="social-square"></span>@tmarrowby</li>
    </ul>
  </section>

  <section class="card card--front" aria-label="Card front">
    <div class="brand-block">
      <div class="mark-square"></div>
      <div class="brand-name">QUORVANT</div>
      <div class="brand-sub">POWER, INC.</div>
    </div>

    <div class="details">
      <div class="detail-row">
        <svg class="detail-icon" viewBox="0 0 34 34" aria-hidden="true">
          <circle cx="17" cy="11" r="7" fill="var(--brand-blue)"/>
          <path d="M3 32 C3 22 10 19 17 19 C24 19 31 22 31 32 Z" fill="var(--brand-blue)"/>
        </svg>
        <span class="detail-rule"></span>
        <div>
          <div class="person-name">DEREK STALLWORTH</div>
          <div class="person-title">Managing Director</div>
        </div>
      </div>

      <div class="detail-row">
        <svg class="detail-icon" viewBox="0 0 34 34" aria-hidden="true">
          <path d="M17 2 C10 2 5 7 5 14 C5 22 17 33 17 33 C17 33 29 22 29 14 C29 7 24 2 17 2 Z" fill="var(--brand-blue)"/>
          <circle cx="17" cy="14" r="5" fill="var(--card)"/>
        </svg>
        <span class="detail-rule"></span>
        <div class="detail-text">48306 Calloway Avenue<br>Westminster, CO 80234</div>
      </div>

      <div class="detail-row">
        <svg class="detail-icon" viewBox="0 0 34 34" aria-hidden="true">
          <g fill="none" stroke="var(--brand-blue)" stroke-width="2.4">
            <circle cx="17" cy="17" r="14"/>
            <ellipse cx="17" cy="17" rx="6" ry="14"/>
            <line x1="3" y1="17" x2="31" y2="17"/>
            <line x1="6" y1="9" x2="28" y2="9"/>
            <line x1="6" y1="25" x2="28" y2="25"/>
          </g>
        </svg>
        <span class="detail-rule"></span>
        <div class="detail-text">555 014 2290<br>derek@quorvantpower.example<br>www.quorvantpower.example</div>
      </div>
    </div>
  </section>
</main>
</body>
</html>
```